Heritage Hollow Business Cards

Require a business card design. <br/><br/>Needs to include logo (either round or long version) plus these details:<br/>Maya Torvel<br/>Heritage Hollow<br/>maya@quonbrook.com.au<br/>02 6481 7390<br/>PO Box Glenwarra NSW 2913<br/>www.heritagehollow.com.au<br/><br/>I need in an editable format so that I can create for multiple staff members. <br/><br/>

Target Market(s)

We are an online store selling renovation products to home owners are builders. Looking for a classic classy design.

Industry/Entity Type

Home And Garden

Contact Information for Business Card

Maya Torvel
Heritage Hollow
maya@quonbrook.com.au
02 6481 7390
PO Box Glenwarra NSW 2913
www.heritagehollow.com.au

Colors

Designer to choose colors to be used in the design.

Requirements
Must have
• Must include Logo.

```html
<!DOCTYPE html>
<html lang="en">
<head>
<meta charset="utf-8">
<title>Heritage Hollow Business Cards</title>
<link rel="stylesheet" href="https://fonts.googleapis.com/css2?family=Gelasio:wght@400;500&display=swap">
<style>
  :root {
    --board: #a5a6aa;
    --shadow: #4a4a4c;
    --card: #f7fbf8;
    --green: #527060;
    --green-text: #567466;
    --grey-text: #5e5e60;
    --tab: #545456;
    --tab-fold: #1e1e20;
    --ink: #232323;
    --white: #ffffff;
  }
  * { margin: 0; padding: 0; box-sizing: border-box; }
  html, body { width: 960px; height: 1200px; overflow: hidden; }
  body {
    position: relative;
    background: var(--board);
    font-family: "Gelasio", Georgia, serif;
  }
  .card-shadow { position: absolute; width: 840px; height: 478px; background: var(--shadow); }
  .card-shadow--front { left: 78px; top: 144px; }
  .card-shadow--back { left: 78px; top: 660px; }
  .card {
    position: absolute; left: 60px; width: 840px; height: 480px;
    background: var(--card); overflow: hidden;
  }
  .card--front { top: 124px; }
  .card--back { top: 640px; }
  .card__texture { position: absolute; inset: 0; background: var(--card); }

  .logo-round {
    position: absolute; left: 134px; top: 115px; width: 232px; height: 232px;
    border: 1.5px solid var(--ink); border-radius: 50%;
    display: flex; align-items: center; justify-content: center; text-align: center;
    font-size: 30px; line-height: 1.1; color: var(--ink);
  }
  .divider { position: absolute; left: 369px; top: 132px; width: 3px; height: 216px; background: var(--green); }

  .person { position: absolute; left: 426px; top: 128px; }
  .person__name { font-size: 35px; color: var(--green-text); line-height: 1.2; }
  .person__company { font-size: 18px; color: var(--grey-text); margin-top: 2px; }

  .contact { position: absolute; left: 426px; font-size: 19px; color: var(--grey-text); display: flex; align-items: center; gap: 14px; }
  .contact svg { width: 18px; height: 18px; flex: none; }
  .contact--email { top: 223px; }
  .contact--phone { top: 254px; }
  .contact--address { top: 304px; }

  .footer-band { position: absolute; left: 0; bottom: 0; width: 100%; height: 58px; background: var(--green); }
  .web-tab { position: absolute; left: 206px; top: 400px; width: 428px; height: 50px; }
  .web-tab__text {
    position: absolute; left: 240px; top: 412px; display: flex; align-items: center; gap: 14px;
    font-size: 19px; color: var(--white);
  }
  .web-tab__text svg { width: 16px; height: 16px; }

  .logo-long {
    position: absolute; left: 0; top: 200px; width: 100%; text-align: center;
    font-size: 56px; color: var(--ink);
  }
</style>
</head>
<body>
  <div class="card-shadow card-shadow--front"></div>
  <section class="card card--front">
    <div class="card__texture" role="img" aria-label="Fine diagonal mint pinstripe background pattern"></div>
    <div class="logo-round">Heritage<br>Hollow</div>
    <div class="divider"></div>
    <div class="person">
      <div class="person__name">Maya Torvel</div>
      <div class="person__company">Heritage Hollow</div>
    </div>
    <div class="contact contact--email">
      <svg viewBox="0 0 18 18"><path d="M1 7 L9 2 L17 7 V16 H1 Z" fill="#567466"/><path d="M3 8 L9 12 L15 8" stroke="#fff" stroke-width="1.5" fill="none"/></svg>
      <span>maya@quonbrook.com.au</span>
    </div>
    <div class="contact contact--phone">
      <svg viewBox="0 0 18 18"><rect x="0" y="0" width="18" height="18" rx="3" fill="#567466"/><path d="M6 4 Q4 9 8 14 L10 13 L9 11 L8 11 Q7 9 7 7 L8 6 L7 4 Z" fill="#fff"/></svg>
      <span>02 6481 7390</span>
    </div>
    <div class="contact contact--address">
      <svg viewBox="0 0 18 18"><path d="M9 1 C5 1 3 4 3 7 C3 11 9 17 9 17 C9 17 15 11 15 7 C15 4 13 1 9 1 Z" fill="#567466"/><circle cx="9" cy="7" r="2.3" fill="#fff"/></svg>
      <span>PO Box Glenwarra NSW 2913</span>
    </div>
    <div class="footer-band"></div>
    <svg class="web-tab" viewBox="0 0 428 50">
      <polygon points="0,0 8,22 0,22" fill="#1e1e20"/>
      <polygon points="428,0 420,22 428,22" fill="#1e1e20"/>
      <polygon points="0,0 428,0 396,50 32,50" fill="#545456"/>
    </svg>
    <div class="web-tab__text">
      <svg viewBox="0 0 16 16" fill="none" stroke="#fff" stroke-width="1.2"><circle cx="8" cy="8" r="7"/><ellipse cx="8" cy="8" rx="3" ry="7"/><path d="M1 8 H15 M2.5 4.5 H13.5 M2.5 11.5 H13.5"/></svg>
      <span>www.heritagehollow.com.au</span>
    </div>
  </section>

  <div class="card-shadow card-shadow--back"></div>
  <section class="card card--back">
    <div class="card__texture" role="img" aria-label="Fine diagonal mint pinstripe background pattern"></div>
    <div class="logo-long">Heritage Hollow</div>
  </section>
</body>
</html>
```